Flyer-Design für Tonwerk Bündnis Kreis
Zielgruppe
Die Tonwerk Bündnis Kreis ist ein Netzwerk von Musikunternehmen [Labels, Musikproduzenten, Promotionagenturen, Verlag, Tonstudios, Werbetexter, Videoproduzenten].
Wir möchten Musikern und Bands die notwendigen Kontakte vermitteln, damit sie ihr Release bestmöglich am Markt platzieren können. Die Idee ist es, die Musik der Bands schon ab Produktionsbeginn durch uns und unsere Kooperationspartner zu screenen und einen ganzheitlichen Produktions-, Distributions- und Marketingmix anzubieten - oder auch nur Teilbereiche, je nachdem wie es die Band wünscht.
Entsprechend soll das Leistungsspektrum auf dem Flyer angezeigt werden auf der Vorderseite und auf der Rückseite zum Einsenden von Demos aufgefordert werden.
Zielgruppe:
Unsere Leistungen richten sich an unabhängige Bands und Künstler, die in Eigenverantwortlichkeit agieren und professionelle Vermarktungsstrukturen nutzen möchten, wie auch Künstler und Bands, die eine Zusammenarbeit mit Labels anstreben. Über unsere Kooperationspartner können wir diverse Genre abdecken, Pop, Singer/Songwriter, Jazz, Rock, Dance, Folk etc.
Stil des Flyers: passend zum Stil der Webseite www.tonwerk-buendnis-kreis.de
monochrom, s/w ggfls. eine Farbe zur Hervorhebung
Format: druckfertige PDF wird benötigt, sowie PDF zum eMail Versand
Ich benötige die Datei als jpg druckfertig
Aufgabenstellung
Inhalte:
> Logo der Tonwerk Bündnis Kreis
> Claim: Ihr habt die songs – wir das professionelle Netzwerk
> Gitarrenfoto s/w
> Webseite: www.tonwerk-buendnis-kreis.de
Leistungen auf der Vorderseite des Flyers (Plakativ darstellen):
Großhandelslistung wie Kaufhallen Rolf, Pelikon etc.
Weltweite digitale Distribution
Eure Musik bei Wendoro, KBT etc.
Promotion in Radio, Print, Web, TV
Studioproduktion
Mixing/Mastering
Pressetexte
Musikvideoproduktion
Labelcodes / ISRC Codes
CD Pressung
Artwork / CD Cover
EPK
Rückseite des Flyers:
Bewerbung physische Demos:
Tonwerk Bündnis Kreis
Artist & Repertoire
Lindacher Gasse 41
D-67312 Worms
Oder
soundfiles und infopaket (Bio, Bandfotos, Konzerthistorie, Discographie)
über cloudserver (z.B. klangbucht, ablagewerk o.ä )

```html
<!DOCTYPE html>
<html lang="de">
<head>
<meta charset="utf-8">
<title>Tonwerk Bündnis Kreis – Flyer</title>
<link href="https://fonts.googleapis.com/css2?family=Ubuntu:wght@300;400;500;700&display=swap" rel="stylesheet">
<style>
  :root {
    --stage: #444444;
    --paper: #ffffff;
    --ink: #333333;
    --ink-soft: #555555;
    --tag: #ffffff;
    --photo-light: #a9a9a9;
    --photo-mid: #6e6e6e;
    --photo-dark: #1e1e1e;
  }
  * { box-sizing: border-box; margin: 0; padding: 0; }
  html, body { width: 918px; height: 1200px; overflow: hidden; background: var(--stage); }
  body { position: relative; font-family: "Ubuntu", sans-serif; color: var(--ink); }

  .flyer { position: absolute; left: 75px; width: 766px; height: 540px; background: var(--paper); overflow: hidden; }
  .flyer--front { top: 48px; }
  .flyer--back { top: 618px; }

  .photo { position: absolute; left: 0; width: 766px; }
  .flyer--front .photo { top: 98px; height: 343px;
    background: radial-gradient(ellipse at 52% 55%, #3a3a3a 0%, #555 22%, transparent 45%),
                linear-gradient(180deg, #b8b8b8 0%, #8f8f8f 40%, #6a6a6a 75%, #4a4a4a 100%); }
  .flyer--back .photo { top: 98px; height: 311px;
    background: radial-gradient(ellipse at 40% 55%, #8a8a8a 0%, #505050 30%, transparent 60%),
                linear-gradient(90deg, #2a2a2a 0%, #3c3c3c 45%, #1e1e1e 75%, #111 100%); }

  .brand-box { position: absolute; left: 25px; top: 0; width: 246px; height: 173px; background: var(--paper);
    box-shadow: 0 2px 6px rgba(0,0,0,.25); display: flex; flex-direction: column; align-items: center; justify-content: center; gap: 10px; z-index: 2; }
  .brand-mark { width: 40px; height: 40px; border: 3px solid var(--ink); border-radius: 50%; }
  .brand-name { font-weight: 700; font-size: 17px; letter-spacing: .3px; text-transform: uppercase; color: var(--ink); text-align: center; line-height: 1.15; }

  .site-url { position: absolute; right: 26px; top: 25px; font-weight: 300; font-size: 13px; color: var(--ink-soft); }

  .tag { position: absolute; background: var(--tag); display: flex; align-items: center; justify-content: center; text-align: center;
    font-size: 11.5px; font-weight: 400; line-height: 1.3; color: var(--ink);
    clip-path: polygon(1% 8%, 4% 0, 30% 4%, 60% 0, 97% 3%, 99% 18%, 97% 35%, 100% 55%, 98% 80%, 100% 96%, 70% 100%, 40% 96%, 6% 100%, 2% 88%, 0 66%, 2% 45%, 0 25%); }

  .claim { position: absolute; left: 0; right: 0; top: 471px; text-align: center; font-size: 23px; font-weight: 400; color: var(--ink); white-space: nowrap; }
  .claim strong { font-weight: 700; font-size: 33px; }

  .coop { position: absolute; left: 528px; top: 236px; width: 203px; text-align: center; z-index: 2; }
  .coop .tag { position: static; height: 45px; font-size: 15px; width: 203px; text-transform: uppercase; }
  .coop-text { margin-top: 10px; font-size: 11.2px; line-height: 15.5px; color: #fff; }

  .contact { position: absolute; top: 430px; }
  .contact--post { left: 37px; }
  .contact--cloud { left: 357px; }
  .contact-head { display: flex; align-items: center; gap: 8px; font-size: 15.5px; font-weight: 400; color: var(--ink); }
  .contact-head small { font-size: 10.5px; font-weight: 300; color: var(--ink-soft); }
  .contact-body { margin-left: 18px; margin-top: 7px; font-size: 11.5px; font-weight: 300; line-height: 15.5px; color: var(--ink-soft); }
  .contact--cloud .contact-body { margin-left: 20px; }
</style>
</head>
<body>

<section class="flyer flyer--front">
  <div class="photo" role="img" aria-label="Schwarz-Weiß-Foto: geöffneter Gitarrenkoffer auf einer Wiese"></div>
  <div class="brand-box">
    <span class="brand-mark"></span>
    <span class="brand-name">Tonwerk Bündnis<br>Kreis</span>
  </div>
  <p class="site-url">www.tonwerk-buendnis-kreis.de</p>

  <div class="tag" style="left:12px;top:234px;width:178px;height:30px;">Labelcodes / ISRC Codes</div>
  <div class="tag" style="left:58px;top:276px;width:178px;height:31px;">CD Pressung &amp;<br>Artwork / CD Cover</div>
  <div class="tag" style="left:12px;top:320px;width:178px;height:31px;">EPK</div>
  <div class="tag" style="left:58px;top:364px;width:178px;height:30px;">Musikvideoproduktion</div>

  <div class="tag" style="left:515px;top:142px;width:189px;height:31px;">Großhandelslistung<br>wie Kaufhallen Rolf, Pelikon etc.</div>
  <div class="tag" style="left:563px;top:186px;width:190px;height:31px;">Weltweite digitale Distribution</div>
  <div class="tag" style="left:515px;top:230px;width:189px;height:29px;">Eure Musik bei Wendoro, KBT etc.</div>
  <div class="tag" style="left:563px;top:273px;width:190px;height:30px;">Promotion in Radio, Print, Web,<br>TV</div>
  <div class="tag" style="left:515px;top:320px;width:189px;height:31px;">Studioproduktion &amp;<br>Mixing/Mastering</div>
  <div class="tag" style="left:563px;top:364px;width:190px;height:30px;">Pressetexte</div>

  <p class="claim">Ihr habt die <strong>SONGS,</strong> wir das professionelle <strong>NETZWERK</strong>.</p>
</section>

<section class="flyer flyer--back">
  <div class="photo" role="img" aria-label="Schwarz-Weiß-Nahaufnahme: Hand greift Akkord auf dem Gitarrenhals mit Kapodaster"></div>
  <div class="brand-box">
    <span class="brand-mark"></span>
    <span class="brand-name">Tonwerk Bündnis<br>Kreis</span>
  </div>
  <p class="site-url">www.tonwerk-buendnis-kreis.de</p>

  <div class="coop">
    <div class="tag">Kooperationspartner<br>gesucht!</div>
    <p class="coop-text">Lust auf eine gemeinsame<br>Zusammenarbeit? Dann meldet<br>euch bei uns – wir suchen noch<br>Kooperationspartner mit der<br>gleichen Leidenschaft für Musik!</p>
  </div>

  <div class="contact contact--post">
    <div class="contact-head">
      <svg width="12" height="18" viewBox="0 0 12 18" aria-hidden="true"><path d="M6 0C2.7 0 0 2.6 0 5.9 0 10.3 6 18 6 18s6-7.7 6-12.1C12 2.6 9.3 0 6 0zm0 8.2a2.4 2.4 0 1 1 0-4.8 2.4 2.4 0 0 1 0 4.8z" fill="#333"/></svg>
      Bewerbung physische Demos
    </div>
    <p class="contact-body">Tonwerk Bündnis Kreis<br>Artist &amp; Repertoire<br>Lindacher Gasse 41<br>D-67312 Worms</p>
  </div>

  <div class="contact contact--cloud">
    <div class="contact-head">
      <svg width="25" height="16" viewBox="0 0 25 16" aria-hidden="true"><path d="M5 16a5 5 0 0 1-.6-9.9A6.5 6.5 0 0 1 16.6 4.4 5.8 5.8 0 1 1 19.2 16z" fill="#333"/></svg>
      Über Cloudserver <small>zB Klangbucht, Ablagewerk...</small>
    </div>
    <p class="contact-body">Soundfiles &amp; Infopaket (Bio, Bandfotos,<br>Konzerthistorie, Discographie) an<br>info@tonwerk-buendnis-kreis.de</p>
  </div>
</section>

</body>
</html>
```